Torvane Travel Business Card Design

We need a new business card design for our travel agency business - Torvane Travel. We design packages to some of the most popular travel destinations in the world for groups, individuals and also tailor-make personalised packages. Our logo attached must be used. On the back of the card we would like a list of all websites under our Torvane brand to be posted. We would like clean, modern, simple design.

Industry/Entity Type

Travel Agent

Contact Information for Business Card

Owen Pridmore
National Sales Manager
Reservations: 1300 742 689
Tel: 61 28473 5096
Fax: 61 2847 3971
Email: owen@torvanetravel.com.au
Web: www.torvanetravel.com.au

Address: Level 1, 417 Harwick Street
Sydney NSW 2000 Australia

Requirements
Must have
• On the back of the card we want all websites listed under our Torvane brand.
• Torvane Travel Group - Wholesale Specialists
• www.qpjourneys.com.au - New Caledonia
• www.bravelmijourneys.com.au - Tahiti
• www.sorvenbreakhub.com.au - China
Nice to have
• Modern, clean lined, simple and fresh
Should not have
• Look dull

```html
<!DOCTYPE html>
<html lang="en">
<head>
<meta charset="utf-8">
<title>Torvane Travel Business Card</title>
<link rel="stylesheet" href="https://fonts.googleapis.com/css2?family=Source+Sans+3:wght@400;600;700&display=swap">
<style>
  :root {
    --backdrop-top: #262626;
    --backdrop-bottom: #060606;
    --card-white: #ffffff;
    --brand-red: #ec2027;
    --brand-red-deep: #c8181e;
    --brand-navy: #2b2a80;
    --ink: #2a2a2a;
  }
  * { margin: 0; padding: 0; box-sizing: border-box; }
  html, body { width: 1200px; height: 900px; overflow: hidden; }
  body {
    position: relative;
    background: linear-gradient(180deg, var(--backdrop-top) 0%, var(--backdrop-bottom) 100%);
    font-family: "Source Sans 3", "Myriad Pro", sans-serif;
  }
  .card {
    position: absolute;
    top: 170px;
    width: 347px;
    height: 561px;
    text-align: center;
  }
  .card-front { left: 259px; background: var(--card-white); color: var(--ink); }
  .card-back { left: 631px; background: var(--brand-red); color: var(--card-white); }

  .accent-tab {
    position: absolute;
    left: 102px;
    width: 143px;
    background: var(--brand-red);
  }
  .accent-tab-top { top: 0; height: 30px; }
  .accent-tab-bottom { bottom: 0; height: 28px; }

  .brand-name {
    position: absolute;
    top: 118px;
    left: 0;
    width: 100%;
    font-size: 46px;
    font-weight: 700;
    letter-spacing: -0.5px;
    color: var(--brand-navy);
    line-height: 1;
  }

  .contact-person {
    position: absolute;
    top: 258px;
    left: 0;
    width: 100%;
    font-size: 15px;
    line-height: 20px;
  }
  .person-name { color: var(--brand-red); font-size: 18px; font-weight: 600; line-height: 24px; }
  .person-role { margin-bottom: 12px; }
  .address { margin-bottom: 15px; }
  .contact-list { list-style: none; }
  .contact-list li { display: flex; justify-content: center; align-items: center; gap: 5px; }
  .label { color: var(--brand-red); }
  .icon { width: 10px; height: 10px; fill: var(--brand-red); flex: none; }

  .hero-area {
    position: absolute;
    top: 100px;
    left: 22px;
    width: 304px;
    height: 135px;
    border-radius: 6px;
    background: var(--brand-red-deep);
  }
  .group-info {
    position: absolute;
    top: 299px;
    left: 0;
    width: 100%;
    font-size: 15px;
    line-height: 20px;
  }
  .group-tagline { margin-bottom: 26px; }
</style>
</head>
<body>
  <section class="card card-front">
    <div class="accent-tab accent-tab-top"></div>
    <div class="brand-name">Torvane Travel</div>

    <div class="contact-person">
      <div class="person-name">Owen Pridmore</div>
      <div class="person-role">National Sales Manager</div>
      <div class="address">Level 1, 417 Harwick Street<br>Sydney NSW 2000 Australia</div>
      <ul class="contact-list">
        <li><span class="label">Reservations:</span> 1300 742 689</li>
        <li>
          <svg class="icon" viewBox="0 0 10 10" aria-hidden="true"><path d="M1 3.5C1 2 2.5 1 5 1s4 1 4 2.5L7.5 4 7 3H3L2.5 4zM2 5h6l1 4H1z"/></svg>
          61 28473 5096
        </li>
        <li>
          <svg class="icon" viewBox="0 0 10 10" aria-hidden="true"><path d="M2 1h5v2H2zM1 3.5h8V9H1zM3 5v1h1V5zm2 0v1h1V5zM3 7v1h1V7zm2 0v1h1V7z"/></svg>
          61 2847 3971
        </li>
        <li>
          <svg class="icon" viewBox="0 0 10 10" aria-hidden="true"><path d="M1 2h8v1L5 5.5 1 3zM1 4l4 2.5L9 4v4H1z"/></svg>
          owen@torvanetravel.com.au
        </li>
        <li>
          <svg class="icon" viewBox="0 0 10 10" aria-hidden="true"><path d="M4 6 6 4M3.5 4.5 2 6a1.4 1.4 0 0 0 2 2l1.5-1.5M6.5 5.5 8 4a1.4 1.4 0 0 0-2-2L4.5 3.5" fill="none" stroke="#ec2027" stroke-width="1.2" stroke-linecap="round"/></svg>
          www.torvanetravel.com.au
        </li>
      </ul>
    </div>

    <div class="accent-tab accent-tab-bottom"></div>
  </section>

  <section class="card card-back">
    <div class="hero-area" role="img" aria-label="Large silhouette of a passenger jet in flight"></div>
    <div class="group-info">
      <div class="group-tagline">Torvane Travel Group<br>Wholesale Specialists</div>
      <ul class="contact-list">
        <li>www.qpjourneys.com.au - New Caledonia</li>
        <li>www.bravelmijourneys.com.au - Tahiti</li>
        <li>www.sorvenbreakhub.com.au - China</li>
      </ul>
    </div>
  </section>
</body>
</html>
```